Flyer für Fußball-Förderverein
Zielgruppe
Wir sind der Fußball-Förderverein des SpVg Halmbeck.
Aufgabenstellung
1. Ziel des Flyers:
Der Flyer soll den Förderverein des SpVg Halmbeck bekannter machen und neue Mitglieder und Sponsoren gewinnen. Er soll darüber informieren, wie der Förderverein den Verein unterstützt und warum eine Mitgliedschaft oder eine Spende wichtig ist.
2. Zielgruppe:
Eltern der Kinder und Jugendlichen, die im SpVg Halmbeck Fußball spielen.
Lokale Unternehmen und potenzielle Sponsoren.
Vereinsmitglieder und Fußballinteressierte in der Region.
3. Hauptbotschaft:
„Unterstütze den SpVg Halmbeck – Gemeinsam für die Zukunft unseres Vereins und der Jugend!“
4. Inhalte:
Über den Förderverein:
Eine kurze Beschreibung des Fördervereins, warum er existiert und was er für den Verein und die Jugend tut.
Mitgliedschaft:
Informationen, wie man Mitglied im Förderverein werden kann. Vorteile und der Beitrag, der benötigt wird.
Spenden:
Möglichkeit der direkten Spende mit einem Hinweis auf steuerliche Vorteile (falls zutreffend). Möglicherweise auch die Angabe eines Spendenkontos.
Beispiele für die Verwendung von Mitteln:
Welche Projekte oder Anschaffungen wurden durch den Förderverein unterstützt (z.B. Trainingsmaterialien, Ausrüstung, Turniere, Jugendfahrten)?
Kontaktinformationen:
Ansprechpartner des Fördervereins mit Telefonnummer, E-Mail-Adresse und eventuell ein Link zur Webseite oder Social-Media-Profilen.
5. Designvorgaben:
Farben und Stil:
Die Vereinsfarben des SpVg Halmbeck sollten im Flyer dominieren (grün-weiß, etc.). Ein modernes, aber sportliches Design, das dynamisch wirkt und die Zielgruppe anspricht.
Logo:
Das Logo des SpVg Halmbeck sollte prominent platziert werden, ebenso das Logo des Fördervereins (falls vorhanden).
Bilder:
Verwendung von Bildern aus dem Vereinsleben, insbesondere von Kindern und Jugendlichen im Spielbetrieb oder bei Vereinsaktivitäten. Falls keine spezifischen Bilder vorhanden sind, können allgemeine Fußballbilde..

```html
<!DOCTYPE html>
<html lang="de">
<head>
<meta charset="utf-8">
<title>Flyer Förderverein SpVg Halmbeck – Vorder- und Rückseite</title>
<link href="https://fonts.googleapis.com/css2?family=Oswald:wght@700&family=Montserrat:wght@500;600;700&display=swap" rel="stylesheet">
<style>
  :root {
    --green: #129a3f;
    --green-dark: #0b6e2b;
    --black: #1c1c1c;
    --white: #ffffff;
    --text: #333333;
    --stage: #c2c2c2;
  }
  * { margin: 0; padding: 0; box-sizing: border-box; }
  html, body { width: 889px; height: 1200px; overflow: hidden; background: var(--stage); }
  .sheet { position: relative; width: 889px; height: 1200px; overflow: hidden; font-family: "Montserrat", sans-serif; color: var(--text); }
  .page { position: absolute; top: 303px; width: 420px; height: 594px; overflow: hidden; background: var(--white); }
  .page--front { left: 12px; }
  .page--back { left: 457px; }
  .page-art { position: absolute; inset: 0; }

  .body-copy { font-size: 6.6px; line-height: 7.6px; font-weight: 500; color: var(--text); white-space: nowrap; }

  /* front */
  .club-mark { position: absolute; display: flex; flex-direction: column; align-items: center; justify-content: center; gap: 12px; }
  .page--front .club-mark { left: 28px; top: 16px; width: 122px; height: 175px; }
  .club-mark .dot { width: 62px; height: 62px; border-radius: 50%; background: var(--green); }
  .club-mark .name { font-weight: 700; font-size: 9px; line-height: 1.3; color: var(--white); text-align: center; text-transform: uppercase; white-space: nowrap; }
  .headline { position: absolute; left: 172px; top: 44px; font-family: "Oswald", sans-serif; font-weight: 700; font-size: 37px; line-height: 0.98; letter-spacing: -0.5px; white-space: nowrap; }
  .headline .lead { display: block; color: var(--white); }
  .headline .club { display: block; color: var(--green); }
  .tagline { position: absolute; left: 173px; top: 124px; font-weight: 600; font-size: 11px; line-height: 12.5px; color: var(--white); white-space: nowrap; }
  .info-panel { position: absolute; left: 26px; top: 194px; width: 196px; height: 320px; background: var(--white); border: 3px solid var(--green); border-radius: 14px; padding: 44px 10px 0 19px; overflow: hidden; }
  .info-panel .panel-title { display: block; width: 151px; background: var(--green); color: var(--white); font-weight: 700; font-size: 17px; line-height: 1.05; padding: 6px 8px 7px 11px; border-radius: 5px; }
  .info-panel .body-copy { margin-top: 8px; }
  .info-panel .section-title { font-weight: 700; font-size: 10px; line-height: 11.5px; color: var(--green); margin-top: 12px; white-space: nowrap; }
  .info-panel .section-title + .body-copy { margin-top: 2px; }
  .website { position: absolute; left: 41px; top: 546px; font-weight: 700; font-size: 13px; color: var(--white); }

  /* back */
  .tab { position: absolute; top: 24px; width: 151px; height: 18px; background: var(--green); color: var(--white); font-weight: 700; font-size: 10.5px; line-height: 18px; text-align: center; border-radius: 3px; }
  .tab--membership { left: 32px; }
  .tab--donation { left: 232px; }
  .loose-copy { position: absolute; top: 51px; }
  .loose-copy--membership { left: 32px; }
  .loose-copy--donation { left: 232px; }
  .card { position: absolute; background: var(--white); border: 2px solid var(--green); border-radius: 10px; }
  .card .card-title { font-weight: 700; font-size: 11px; line-height: 12px; color: var(--green); white-space: nowrap; }
  .card .body-copy { margin-top: 3px; }
  .card--examples { left: 219px; top: 90px; width: 184px; height: 88px; padding: 10px 8px 0 13px; }
  .card--benefits { left: 18px; top: 122px; width: 182px; height: 142px; padding: 11px 8px 0 13px; }
  .page--back .club-mark { left: 240px; top: 195px; width: 151px; height: 200px; }
  .page--back .club-mark .dot { width: 80px; height: 80px; }
  .page--back .club-mark .name { font-size: 9.5px; }
  .contact-note { position: absolute; left: 0; top: 524px; width: 420px; text-align: center; font-weight: 600; font-size: 8px; line-height: 10px; color: var(--white); }
  .contact-bar { position: absolute; left: 29px; top: 553px; width: 364px; height: 22px; border: 2px solid var(--green); border-radius: 11px; display: flex; align-items: center; justify-content: center; gap: 6px; font-weight: 700; font-size: 8px; color: var(--white); white-space: nowrap; }
  .contact-bar .item { display: flex; align-items: center; gap: 3px; }
  .contact-bar svg { width: 8px; height: 8px; }
  .contact-bar .sep { color: #8a8a8a; font-weight: 500; }
</style>
</head>
<body>
<div class="sheet">

  <!-- Vorderseite -->
  <article class="page page--front">
    <svg class="page-art" width="420" height="594" viewBox="0 0 420 594">
      <defs>
        <linearGradient id="frontScene" x1="0" y1="0" x2="0" y2="1">
          <stop offset="0" stop-color="#5fa6e0"/>
          <stop offset="0.2" stop-color="#cfe3f1"/>
          <stop offset="0.42" stop-color="#7f9aa8"/>
          <stop offset="0.56" stop-color="#4a6e55"/>
          <stop offset="0.66" stop-color="#3f9336"/>
          <stop offset="1" stop-color="#2e7f28"/>
        </linearGradient>
        <linearGradient id="playerTone" x1="0" y1="0" x2="0" y2="1">
          <stop offset="0" stop-color="#1f9a45"/>
          <stop offset="1" stop-color="#136b30"/>
        </linearGradient>
      </defs>
      <rect width="420" height="594" fill="url(#frontScene)" role="img" aria-label="Fotografie: Fußballstadion mit Himmel und Rasen"/>
      <rect x="262" y="230" width="130" height="330" rx="60" fill="url(#playerTone)" opacity="0.6" role="img" aria-label="Fotografie: junger Fußballspieler im grünen Trikot beim Ballannehmen"/>
      <path d="M0 89 Q170 36 420 24 L420 166 Q210 166 0 222 Z" fill="var(--black)"/>
      <path d="M150 40 Q290 16 420 16" fill="none" stroke="var(--white)" stroke-width="3"/>
      <path d="M0 222 Q210 166 420 166 L420 178 Q210 180 0 236 Z" fill="var(--green)"/>
      <path d="M0 236 Q210 180 420 178 L420 182 Q210 185 0 241 Z" fill="var(--white)"/>
    </svg>

    <div class="club-mark">
      <span class="dot"></span>
      <span class="name">Fußball Förderverein<br>Halmbeck e.V.</span>
    </div>

    <h1 class="headline">
      <span class="lead">Unterstütze den</span>
      <span class="club">SpVg Halmbeck</span>
    </h1>
    <p class="tagline">Gemeinsam für die Zukunft unseres<br>Vereins und der Jugend!</p>

    <section class="info-panel">
      <h2 class="panel-title">Über den<br>Förderverein:</h2>
      <p class="body-copy">Lorem ipsum dolor sit amet, consectetur<br>adipiscing elit, sed do eiusmod tempor<br>incididunt ut labore et dolore magna aliqua.<br>Ut enim ad minim veniam, quis nostrud<br>exercitation ullamco laboris nisi ut aliquip<br>ex ea commodo consequat. Duis aute irure<br>dolor in reprehenderit in voluptate velit<br>esse cillum dolore eu fugiat nulla pariatur.</p>
      <h3 class="section-title">Vorteile für Vereine und<br>Jugendliche:</h3>
      <p class="body-copy">Lorem ipsum dolor sit amet, consectetur<br>adipiscing elit, sed do eiusmod tempor<br>incididunt ut labore et dolore magna aliqua.<br>Ut enim ad minim veniam, quis nostrud<br>exercitation ullamco laboris nisi ut aliquip<br>ex ea commodo consequat.</p>
      <p class="body-copy">Lorem ipsum dolor sit amet, consectetur<br>adipiscing elit, sed do eiusmod tempor<br>incididunt ut labore et dolore magna aliqua.<br>Ut enim ad minim veniam, quis nostrud<br>exercitation ullamco laboris nisi ut aliquip<br>ex ea commodo consequat.</p>
    </section>

    <p class="website">www.spvg-halmbeck.de</p>
  </article>

  <!-- Rückseite -->
  <article class="page page--back">
    <svg class="page-art" width="420" height="594" viewBox="0 0 420 594">
      <defs>
        <linearGradient id="backScene" x1="0" y1="0" x2="0" y2="1">
          <stop offset="0" stop-color="#a9cfee"/>
          <stop offset="0.12" stop-color="#e6eef2"/>
          <stop offset="0.3" stop-color="#8da3ad"/>
          <stop offset="0.42" stop-color="#5d8a4c"/>
          <stop offset="0.6" stop-color="#6fb83a"/>
          <stop offset="1" stop-color="#4f9a2c"/>
        </linearGradient>
        <linearGradient id="circleTone" x1="0" y1="0" x2="0" y2="1">
          <stop offset="0" stop-color="#8fc46a"/>
          <stop offset="1" stop-color="#3f8f33"/>
        </linearGradient>
      </defs>
      <rect width="420" height="594" fill="url(#backScene)" role="img" aria-label="Fotografie: Stadion mit Tribüne und Rasen"/>
      <path d="M0 370 Q140 300 240 285 L420 280 L420 480 L0 480 Z" fill="#5f9a4a" opacity="0.55" role="img" aria-label="Fotografie: Kinder beim Fußballtraining"/>
      <path d="M0 352 Q120 296 250 276 L250 288 Q120 308 0 366 Z" fill="var(--green)"/>
      <path d="M0 366 Q120 308 250 288 L250 292 Q120 313 0 371 Z" fill="var(--white)"/>
      <path d="M0 468 Q210 452 420 466 L420 594 L0 594 Z" fill="var(--black)"/>
      <g stroke="var(--black)" stroke-width="4" fill="url(#circleTone)">
        <circle cx="72" cy="461" r="46" role="img" aria-label="Fotografie: Taktiktafel im Training"/>
        <circle cx="163" cy="461" r="46" role="img" aria-label="Fotografie: Jugendspieler am Ball"/>
        <circle cx="254" cy="461" r="46" role="img" aria-label="Fotografie: Übung mit Hütchen"/>
        <circle cx="347" cy="461" r="46" role="img" aria-label="Fotografie: Spieler beim Dribbling"/>
      </g>
    </svg>

    <h2 class="tab tab--membership">Mitgliedschaft:</h2>
    <p class="body-copy loose-copy loose-copy--membership">Lorem ipsum dolor sit amet, consectetur<br>adipiscing elit, sed do eiusmod tempor<br>incididunt ut labore et dolore magna aliqua.<br>Ut enim ad minim veniam, quis nostrud<br>exercitation ullamco laboris nisi ut aliquip<br>ex ea commodo consequat. Duis aute irure<br>dolor in reprehenderit in voluptate velit<br>esse cillum dolore eu fugiat nulla pariatur.</p>

    <h2 class="tab tab--donation">Spenden:</h2>
    <p class="body-copy loose-copy loose-copy--donation">Möglichkeit der direkten Spende<br>mit einem Hinweis auf steuerliche Vorteile<br>(falls zutreffend). Möglicherweise auch die<br>Angabe eines Spendenkontos.</p>

    <section class="card card--examples">
      <h3 class="card-title">Beispiele für die<br>Verwendung von Mitteln:</h3>
      <p class="body-copy">Welche Projekte oder Anschaffungen<br>wurden durch den Förderverein unterstützt<br>(z.B. Trainingsmaterialien, Ausrüstung,<br>Turniere, Jugendfahrten)?</p>
    </section>

    <section class="card card--benefits">
      <h3 class="card-title">Vorteile und der Beitrag,<br>der benötigt wird.</h3>
      <p class="body-copy">Lorem ipsum dolor sit amet, consectetur<br>adipiscing elit, sed do eiusmod tempor<br>incididunt ut labore et dolore magna aliqua.<br>Ut enim ad minim veniam, quis nostrud<br>exercitation ullamco laboris nisi ut aliquip<br>ex ea commodo consequat. Duis aute irure<br>dolor in reprehenderit in voluptate velit<br>esse cillum dolore eu fugiat nulla pariatur.<br>Excepteur sint occaecat cupidatat non<br>proident, sunt in culpa qui officia deserunt<br>mollit anim id est laborum.</p>
    </section>

    <div class="club-mark">
      <span class="dot"></span>
      <span class="name">Fußball Förderverein<br>Halmbeck e.V.</span>
    </div>

    <p class="contact-note">Ansprechpartner des Fördervereins mit Telefonnummer, E-Mail-Adresse und<br>eventuell ein Link zur Webseite oder Social-Media-Profilen.</p>

    <div class="contact-bar">
      <span class="item">
        <svg viewBox="0 0 10 10"><circle cx="5" cy="5" r="5" fill="#fff"/><path d="M3.2 2.6 L4.2 2.5 L4.6 3.8 L4 4.3 Q4.5 5.5 5.7 6 L6.2 5.4 L7.5 5.8 L7.4 6.8 Q5.8 7.6 4 6 Q2.5 4.3 3.2 2.6Z" fill="var(--black)"/></svg>
        123-456-7890
      </span>
      <span class="sep">|</span>
      <span class="item">
        <svg viewBox="0 0 10 10"><circle cx="5" cy="5" r="5" fill="#fff"/><circle cx="5" cy="5" r="3" fill="none" stroke="var(--black)" stroke-width="0.8"/><path d="M2 5 H8 M5 2 V8" stroke="var(--black)" stroke-width="0.7"/></svg>
        spvg-halmbeck.de
      </span>
      <span class="sep">|</span>
      <span class="item">
        <svg viewBox="0 0 10 10"><circle cx="5" cy="5" r="5" fill="#fff"/><rect x="2.5" y="3.3" width="5" height="3.6" fill="none" stroke="var(--black)" stroke-width="0.7"/><path d="M2.5 3.3 L5 5.3 L7.5 3.3" fill="none" stroke="var(--black)" stroke-width="0.7"/></svg>
        info@spvg-halmbeck.de
      </span>
    </div>
  </article>

</div>
</body>
</html>
```